Tending Our Garden eBook Cover Design

I want to deisgn a cover for my eBook (FRONT COVER) and the title is:

What I Grew From a Single Spark. And Why It Matters
By KT Dorran

TITLE CHANGED TO: UNDER THE WILLOW TREE; WHERE I FOUND MY QUIET STRENGTH AND WHERE YOU MIGHT TOO

The color palette is attached. Along with some photos options of me. Along with the ebook in WORD Document. My website is www.KTDorranLive.example. You can use a different color palette if you think it is best

Target Market(s)

women who look to build a personal brand

Industry/Entity Type

health and wellness

Requirements
Must have
• the title
Nice to have
• use my picture on the cover; but that is optional
Should not have
• any men

```html
<!DOCTYPE html>
<html lang="en">
<head>
<meta charset="utf-8">
<title>Under the Willow Tree — KT Dorran</title>
<link href="https://fonts.googleapis.com/css2?family=Montserrat:wght@500;600&family=Saira+Condensed:wght@600&display=swap" rel="stylesheet">
<style>
  :root {
    --page: #ffffff;
    --ink-dark: #08131a;
    --band: #0b1820;
    --pink: #eca2ad;
    --peach: #f7d6cc;
    --white: #ffffff;
    --rule: #c9ccd0;
  }
  html, body {
    margin: 0;
    width: 1200px;
    height: 1200px;
    overflow: hidden;
    background: var(--page);
  }
  .cover {
    position: absolute;
    left: 224px;
    top: 36px;
    width: 752px;
    height: 1128px;
    background: var(--ink-dark);
    overflow: hidden;
  }
  .cover__photo {
    position: absolute;
    left: 0;
    top: 340px;
    width: 752px;
    height: 740px;
    background:
      radial-gradient(ellipse 150px 230px at 350px 470px, rgba(214, 48, 32, 0.85), rgba(214, 48, 32, 0) 100%),
      radial-gradient(ellipse 420px 260px at 620px 700px, rgba(205, 212, 218, 0.55), rgba(205, 212, 218, 0) 100%),
      linear-gradient(180deg, var(--ink-dark) 0%, #17191c 35%, #2a2422 70%, #3a3431 100%);
  }
  .title {
    position: absolute;
    left: 0;
    width: 100%;
    margin: 0;
    text-align: center;
    white-space: nowrap;
  }
  .title--lead {
    top: 20px;
    height: 48px;
    line-height: 48px;
    font: 500 42px/48px "Montserrat", sans-serif;
    color: var(--white);
  }
  .title--big {
    font-family: "Saira Condensed", sans-serif;
    font-weight: 600;
    letter-spacing: 1px;
  }
  .title--line2 {
    top: 82px;
    height: 100px;
    font-size: 88px;
    line-height: 100px;
    color: var(--pink);
  }
  .title--line3 {
    top: 196px;
    height: 106px;
    font-size: 100px;
    line-height: 106px;
    color: var(--peach);
  }
  .title--line5 {
    top: 378px;
    height: 86px;
    font-size: 78px;
    line-height: 86px;
    color: var(--pink);
  }
  .connector {
    position: absolute;
    top: 316px;
    left: 0;
    width: 100%;
    height: 44px;
    display: flex;
    align-items: center;
    justify-content: center;
    gap: 12px;
  }
  .connector__rule {
    width: 128px;
    height: 1px;
    background: var(--rule);
  }
  .connector__word {
    font: 500 46px/44px "Montserrat", sans-serif;
    color: var(--white);
  }
  .byline {
    position: absolute;
    left: 0;
    bottom: 0;
    width: 100%;
    height: 52px;
    background: var(--band);
    display: flex;
    align-items: center;
    justify-content: center;
    gap: 10px;
    font-family: "Montserrat", sans-serif;
    font-weight: 600;
    color: var(--peach);
    letter-spacing: 3px;
  }
  .byline__by { font-size: 22px; }
  .byline__name { font-size: 32px; }
</style>
</head>
<body>
  <div class="cover">
    <div class="cover__photo" role="img" aria-label="Photo of the author seated in a director's chair, wearing a red dress, in a dark studio"></div>

    <h1 class="title title--lead">UNDER THE WILLOW TREE;</h1>
    <p class="title title--big title--line2">WHERE I FOUND MY</p>
    <p class="title title--big title--line3">QUIET STRENGTH</p>

    <div class="connector">
      <span class="connector__rule"></span>
      <span class="connector__word">AND</span>
      <span class="connector__rule"></span>
    </div>

    <p class="title title--big title--line5">WHERE YOU MIGHT TOO</p>

    <div class="byline">
      <span class="byline__by">BY</span>
      <span class="byline__name">KT DORRAN</span>
    </div>
  </div>
</body>
</html>
```